Brantley Advisory Group provides support for renewable energy projects to utilities and suppliers

I need a professional looking business card that is both simple and elegant and unique. My clients are mostly large organizations not individuals. I am a consultant with my own company that is small but would like to give clients the impression I am larger. Smart grid, fiber optics, software, field hardware, distribution automation, substation automation, operations, energy storage/batteries, microgrids, customer service, strategy/roadmaps, conservation, Automated Metering Infrastruture (AMI or smart meters) are all areas of focus.

Target Market(s)

Utilities, suppliers, governmental agencies involved in energy. All types of energy especially natural gas and electrical. Especially renewable energy or green projects.

Contact Information for Business Card

Name - Corwin Ashdale Cell Phone - 425.318.2746 Email - mbrantley@brantleyag-example.com
Company - Brantley Advisory Group (logo) Title - Principal

Font styles to use
Serif
Sans Serif

Colors

Designer to choose colors to be used in the design.

Requirements
Must have
• Simple and professional and powerful.
• Unique/creative design.
Nice to have
• Utilize color scheme to accent logo colors. Maybe some geometric pattern on edge of card with color.
Should not have
• Busy, complicated, traditional

```html
<!DOCTYPE html>
<html lang="en">
<head>
<meta charset="utf-8">
<title>Brantley Advisory Group – Business Card</title>
<link rel="stylesheet" href="https://fonts.googleapis.com/css2?family=Montserrat:wght@600;700&family=Poppins:wght@400;500&display=swap">
<style>
  :root {
    --page: #ffffff;
    --card-front: #ececec;
    --card-back: #f7f7f7;
    --slate: #6b7f8a;
    --teal: #3fe0d6;
    --teal-deep: #10aca0;
    --navy: #163a4f;
    --mist: #e3ecec;
    --brand-blue: #1d1b9c;
    --ink: #222222;
  }
  * { margin: 0; padding: 0; box-sizing: border-box; }
  html, body {
    width: 1200px; height: 1200px; overflow: hidden;
    background: var(--page);
  }
  .canvas { position: relative; width: 1200px; height: 1200px; }
  .card {
    position: absolute; left: 244px;
    width: 603px; height: 345px;
    transform: scale(1.25); transform-origin: top left;
    overflow: hidden;
    box-shadow: 0 4px 14px rgba(60, 70, 90, 0.28);
  }
  .card--front { top: 128px; background: linear-gradient(180deg, #e6e6e6 0%, var(--card-front) 60%); }
  .card--back { top: 625px; background: linear-gradient(180deg, var(--mist) 0%, var(--card-back) 48%); }

  .accent { position: absolute; }
  .accent--front-top {
    right: 0; top: 0; width: 250px; height: 140px;
    background: linear-gradient(100deg, rgba(63, 224, 214, 0) 0%, var(--teal) 45%, var(--slate) 100%);
    opacity: 0.85;
  }
  .accent--front-bottom {
    left: 0; bottom: 0; width: 300px; height: 97px;
    background: linear-gradient(80deg, var(--slate) 0%, var(--teal) 70%, rgba(63, 224, 214, 0) 100%);
    opacity: 0.85;
  }
  .accent--back-top {
    right: 0; top: 8px; width: 200px; height: 134px;
    background: linear-gradient(100deg, rgba(16, 172, 160, 0) 0%, var(--teal-deep) 40%, var(--navy) 100%);
  }
  .accent--back-bottom {
    left: 0; bottom: 0; width: 510px; height: 73px;
    background: linear-gradient(90deg, var(--teal-deep) 0%, var(--navy) 45%, var(--navy) 75%, rgba(16, 172, 160, 0) 100%);
  }

  .front-brand {
    position: absolute; left: 0; right: 0; top: 150px;
    display: flex; align-items: center; justify-content: center; gap: 12px;
  }
  .front-brand__mark { width: 28px; height: 28px; background: var(--brand-blue); }
  .front-brand__name {
    font-family: "Montserrat", sans-serif; font-weight: 700;
    font-size: 28px; color: var(--brand-blue);
  }

  .holder-name {
    position: absolute; left: 33px; top: 44px;
    font-family: "Montserrat", sans-serif; font-weight: 700;
    font-size: 37px; color: var(--ink);
  }
  .back-brand {
    position: absolute; left: 18px; top: 196px;
    display: flex; align-items: center; gap: 7px;
  }
  .back-brand__mark { width: 26px; height: 26px; border: 2.5px solid var(--ink); }
  .back-brand__name {
    font-family: "Montserrat", sans-serif; font-weight: 700;
    font-size: 14px; line-height: 16px; color: var(--ink);
  }
  .contact {
    position: absolute; display: flex; align-items: flex-start; gap: 9px;
    font-family: "Poppins", sans-serif; color: var(--ink);
  }
  .contact svg { flex: none; width: 12px; height: 12px; fill: var(--ink); }
  .contact span { line-height: 12px; }
  .contact--phone { left: 196px; top: 212px; font-size: 9.5px; }
  .contact--email { left: 196px; top: 240px; font-size: 8px; }
  .contact--web, .contact--address {
    font-size: 6.5px; letter-spacing: 2px; font-weight: 500;
  }
  .contact--address span { line-height: 10px; }
  .contact--web { left: 405px; top: 210px; }
  .contact--address { left: 405px; top: 238px; }
</style>
</head>
<body>
<main class="canvas">

  <section class="card card--front" aria-label="Card front">
    <div class="accent accent--front-top" role="img" aria-label="Angular teal and slate accent bands"></div>
    <div class="accent accent--front-bottom" role="img" aria-label="Angular slate and teal accent bands"></div>
    <div class="front-brand">
      <span class="front-brand__mark"></span>
      <span class="front-brand__name">Brantley Advisory Group</span>
    </div>
  </section>

  <section class="card card--back" aria-label="Card back">
    <div class="accent accent--back-top" role="img" aria-label="Angular navy and teal accent bands"></div>
    <div class="accent accent--back-bottom" role="img" aria-label="Angular navy and teal accent bands"></div>

    <h1 class="holder-name">Corwin Ashdale</h1>

    <div class="back-brand">
      <span class="back-brand__mark"></span>
      <span class="back-brand__name">Brantley<br>Advisory Group</span>
    </div>

    <div class="contact contact--phone">
      <svg viewBox="0 0 24 24"><path d="M6.6 10.8a15 15 0 0 0 6.6 6.6l2.2-2.2a1 1 0 0 1 1-.25 11.4 11.4 0 0 0 3.6.57 1 1 0 0 1 1 1V20a1 1 0 0 1-1 1A17 17 0 0 1 3 4a1 1 0 0 1 1-1h3.5a1 1 0 0 1 1 1c0 1.25.2 2.45.57 3.57a1 1 0 0 1-.25 1z"/></svg>
      <span>425.318.2746</span>
    </div>
    <div class="contact contact--email">
      <svg viewBox="0 0 24 24"><path d="M2 5h20v14H2zm2 2v.4l8 5.2 8-5.2V7zm16 2.8-8 5.2-8-5.2V17h16z"/></svg>
      <span>mbrantley@brantleyag-example.com</span>
    </div>
    <div class="contact contact--web">
      <svg viewBox="0 0 24 24"><path d="M12 2a10 10 0 1 0 0 20 10 10 0 0 0 0-20zm0 2a13 13 0 0 1 1.9 4h-3.8A13 13 0 0 1 12 4zM4.3 14a8 8 0 0 1 0-4h3.3a16 16 0 0 0 0 4zm5.4 0a14 14 0 0 1 0-4h4.6a14 14 0 0 1 0 4zm6.7 0a16 16 0 0 0 0-4h3.3a8 8 0 0 1 0 4zM12 20a13 13 0 0 1-1.9-4h3.8A13 13 0 0 1 12 20z"/></svg>
      <span>WWW.COMPANYNAME.COM</span>
    </div>
    <div class="contact contact--address">
      <svg viewBox="0 0 24 24"><path d="M12 2a7 7 0 0 0-7 7c0 5.2 7 13 7 13s7-7.8 7-13a7 7 0 0 0-7-7zm0 9.5A2.5 2.5 0 1 1 12 6.5a2.5 2.5 0 0 1 0 5z"/></svg>
      <span>1234 YOUR LOCATION HERE<br>YOUR RD. YOUR STREET<br>POSTAL 00000</span>
    </div>
  </section>

</main>
</body>
</html>
```